Young, modern, highly skilled carpenter needs business card design

I need a business card design for my construction business. Its called 'Pemberton Building Partners'. Im looking for a ultra modern design that incorporates P B P, the first letters of the name with only a subtle reference to carpentry. The design should reflect my high quality work and eye for detail. i have also uploaded some exmaple designs i like.

Industry/Entity Type

Construction

Requirements
Must have
• Name of business, my name, mobile number, ABN number, email address
Nice to have
• A logo incorporating the name of the business

```html
<!DOCTYPE html>
<html lang="en">
<head>
<meta charset="utf-8">
<title>Pemberton Building Partners – Business Card</title>
<link rel="stylesheet" href="https://fonts.googleapis.com/css2?family=Cabin:wght@400&display=swap">
<style>
  :root {
    --backdrop: #e6ecec;
    --card-front: #151515;
    --card-back: #c9b262;
    --card-back-light: #d2bc6c;
    --gold: #c3a956;
    --ink: #141414;
  }
  * { margin: 0; padding: 0; box-sizing: border-box; }
  html, body {
    width: 1200px;
    height: 900px;
    overflow: hidden;
    background: var(--backdrop);
    font-family: "Cabin", sans-serif;
  }
  .stage {
    position: relative;
    width: 1200px;
    height: 900px;
  }
  .card {
    position: absolute;
    left: 334px;
    width: 542px;
    height: 371px;
  }
  .card--front {
    top: 61px;
    background: var(--card-front);
  }
  .card--back {
    top: 460px;
    background: radial-gradient(ellipse at 40% 40%, var(--card-back-light), var(--card-back));
    color: var(--ink);
  }
  .monogram {
    position: absolute;
    left: 0;
    right: 0;
    top: 164px;
    text-align: center;
    color: var(--gold);
    font-size: 50px;
    font-weight: 400;
    letter-spacing: 6px;
    line-height: 1;
  }
  .business-name {
    position: absolute;
    left: 65px;
    top: 76px;
    font-size: 21px;
    font-weight: 400;
    letter-spacing: 0.5px;
    text-transform: uppercase;
    line-height: 1;
  }
  .contact {
    position: absolute;
    left: 65px;
    top: 217px;
    list-style: none;
    font-size: 19px;
    line-height: 26.5px;
  }
</style>
</head>
<body>
  <main class="stage">
    <section class="card card--front" aria-label="Card front">
      <p class="monogram">PBP</p>
    </section>

    <section class="card card--back" aria-label="Card back">
      <h1 class="business-name">Pemberton Building Partners</h1>
      <ul class="contact">
        <li class="contact__name">Liam Pemberton</li>
        <li class="contact__email">M: liam_pemberton@mailbox.com</li>
        <li class="contact__phone">T: 0418365204</li>
        <li class="contact__abn">ABN: 51 824 307 962</li>
      </ul>
    </section>
  </main>
</body>
</html>
```